CRPG is needing business cards, and stationary created.

Pixel Forge created a logo for our business, and now we are wanting business cards, and stationary. I have included two designs of the same logo. Please feel free to use them as you want. The name of the company is Cedar Ridge Property Group LLC, the address is 812 NE Willow Ln., Suite 9, the city & state is Bend, Oregon, zip code is 97815, Telephone number is 541-327-4489, Fax number is 541-327-6051, the name on the business card is Carl Whitby CMCA

Industry/Entity Type

Property Management

Contact Information for Business Card

The card needs to look professional. Upscale.

Requirements
Must have
• The colors we are using are on the logo that has been uploaded.

```html
<!DOCTYPE html>
<html lang="en">
<head>
<meta charset="UTF-8">
<title>Cedar Ridge Property Group — Letterhead</title>
<link href="https://fonts.googleapis.com/css2?family=Open+Sans:wght@400;600;700&display=swap" rel="stylesheet">
<style>
  :root {
    --backdrop: #b9c2bb;
    --paper: #ffffff;
    --brand-green: #1f8a6e;
    --brand-slate: #2f3a44;
    --ink: #1f1f1f;
    --rule: #4a5560;
  }
  * { box-sizing: border-box; margin: 0; padding: 0; }
  html, body {
    width: 1200px; height: 910px; overflow: hidden;
    background: var(--backdrop);
    font-family: "Open Sans", Arial, sans-serif;
    color: var(--ink);
  }
  .letterhead {
    position: absolute; left: 296px; top: 25px;
    width: 608px; height: 860px;
    background: var(--paper);
    box-shadow: 0 4px 18px rgba(0,0,0,0.18);
    padding: 40px 50px;
  }
  .header { display: flex; justify-content: space-between; align-items: flex-start; height: 110px; }
  .brand { display: flex; align-items: center; gap: 10px; margin-top: 38px; }
  .brand-mark { width: 26px; height: 26px; background: var(--brand-green); }
  .brand-name { font-weight: 700; font-size: 17px; color: var(--brand-green); letter-spacing: 0.3px; }
  .contact { display: flex; gap: 14px; align-items: flex-start; }
  .contact-divider { width: 1px; height: 66px; background: var(--rule); margin-top: 4px; }
  .contact-list { list-style: none; font-size: 8.5px; line-height: 15px; color: var(--brand-slate); }
  .contact-list li { display: flex; align-items: center; gap: 6px; }
  .contact-list svg { width: 8px; height: 8px; fill: var(--brand-green); }
  .letter { font-size: 11.5px; line-height: 1.65; margin-top: 22px; }
  .date { margin-bottom: 26px; }
  .recipient { margin-bottom: 26px; }
  .salutation { margin-bottom: 2px; }
  .letter p.body { margin-bottom: 22px; text-align: justify; width: 470px; }
  .closing { margin-top: 34px; }
  .signer { margin-top: 22px; font-weight: 700; }
  .footer {
    position: absolute; right: 40px; bottom: 40px; left: 40px;
    display: flex; align-items: flex-end; gap: 10px;
  }
  .footer-rule { height: 1px; background: var(--rule); margin-bottom: 6px; }
  .footer-rule.lead { flex: 1; }
  .footer-rule.tail { width: 40px; }
  .footer-text { text-align: right; font-size: 9.5px; line-height: 1.45; color: var(--brand-slate); }
  .footer-company { font-weight: 700; color: var(--brand-green); }
</style>
</head>
<body>
  <main class="letterhead">
    <header class="header">
      <div class="brand">
        <span class="brand-mark"></span>
        <span class="brand-name">Cedar Ridge Property Group</span>
      </div>
      <div class="contact">
        <span class="contact-divider"></span>
        <ul class="contact-list">
          <li><svg viewBox="0 0 10 10"><path d="M2 1l2 2-1 1.5c.7 1.3 1.5 2.1 2.5 2.5L7 6l2 2-1.5 1.5C4 9 1 6 .5 2.5z"/></svg>541-327-4489</li>
          <li><svg viewBox="0 0 10 10"><rect x="1" y="3" width="8" height="5"/><rect x="3" y="1" width="4" height="2"/></svg>541-327-6051</li>
          <li><svg viewBox="0 0 10 10"><rect x="0.5" y="2" width="9" height="6"/></svg>info@cedarridgepg.com</li>
          <li><svg viewBox="0 0 10 10"><circle cx="5" cy="5" r="4.5"/></svg>www.cedarridgepg.com</li>
        </ul>
      </div>
    </header>

    <section class="letter">
      <p class="date">Date: 20 November 2018</p>
      <p class="recipient">To<br>Maple Court Gardens Ltd.<br>58 Linden Row, Suite# B<br>Portland, OR 97204</p>
      <p class="salutation">Dear Harlow,</p>
      <p class="body">Lorem Ipsum is simply dummy text of the printing and typesetting industry. Lorem Ipsum has been the industry's standard dummy text ever since the 1500s, when an unknown printer took a galley of type and scrambled it to make a type specimen book. It has survived not only five centuries, but also the leap into electronic typesetting, remaining essentially unchanged. It was popularised in the 1960s with the release of Typemark sheets containing Lorem Ipsum passages, and more recently with desktop publishing software like Quillset Composer including versions of Lorem Ipsum.</p>
      <p class="body">Lorem Ipsum is simply dummy text of the printing and typesetting industry. Lorem Ipsum has been the industry's.</p>
      <p class="closing">Thanking you</p>
      <p class="signer">Carl Whitby</p>
      <p class="title">CMCA</p>
    </section>

    <footer class="footer">
      <span class="footer-rule lead"></span>
      <div class="footer-text">
        <div class="footer-company">Cedar Ridge Property Group LLC</div>
        <div>812 NE Willow Ln., Suite 9, the city &amp; state is Bend, Oregon, zip code is 97815</div>
      </div>
      <span class="footer-rule tail"></span>
    </footer>
  </main>
</body>
</html>
```